Designing a label for Convertible Hood Cleaner (also 6 more labels to design in the future)

We have a range of cleaning products which we need to update label designs

This competition is just for one design but once a winner has been selected we have a lot more work for you including 6 more labels and a new logo.

Please see files for content. This product is very popular but the label is outdated.

Size of label - 110mm x 75mm
This will be a sticky label to be added to a sachet (white ziplock pouch)

Colors

Designer to choose colors to be used in the design.

```html
<!DOCTYPE html>
<html lang="en">
<head>
<meta charset="utf-8">
<title>Heavy Duty Convertible Soft Top Cleaner – Sachet Label</title>
<link href="https://fonts.googleapis.com/css2?family=Open+Sans:ital,wght@0,400;0,700;0,800;1,800&family=Russo+One&display=swap" rel="stylesheet">
<style>
  :root {
    --page-bg: #ffffff;
    --ink: #111111;
    --sky-light: #d4f1fb;
    --sky-mid: #6fcbef;
    --ocean: #1578cf;
    --navy: #061a52;
    --black: #000000;
    --brand-ink: #0b2a6b;
    --heading-orange: #f6a623;
    --heading-yellow: #f7d81c;
    --heading-red: #e2352c;
    --outline-dark: #1b1b1b;
    --tag-yellow: #f8e11e;
    --badge-pink: #e4245b;
    --bullet-orange: #f0592a;
    --rule-blue: #8fd3f3;
    --white: #ffffff;
    --photo-top: #e9eef2;
    --photo-mid: #c8d0d8;
    --photo-roof: #b54a4a;
  }

  * { box-sizing: border-box; margin: 0; padding: 0; }

  html, body {
    width: 1200px;
    height: 1000px;
    overflow: hidden;
    background: var(--page-bg);
  }

  .artboard {
    position: relative;
    width: 1200px;
    height: 1000px;
  }

  .spec-note {
    position: absolute;
    top: 140px;
    left: 0;
    width: 1190px;
    text-align: center;
    font-family: "Open Sans", sans-serif;
    font-size: 26px;
    color: var(--ink);
  }

  .label {
    position: absolute;
    left: 355px;
    top: 196px;
    width: 484px;
    height: 689px;
    overflow: hidden;
    border: 1px solid #222;
    background:
      radial-gradient(ellipse 60% 45% at 30% 40%, rgba(255,255,255,0.75), rgba(255,255,255,0) 70%),
      radial-gradient(ellipse 80% 60% at 85% 55%, rgba(20,100,210,0.55), rgba(20,100,210,0) 70%),
      linear-gradient(100deg, var(--sky-light) 0%, var(--sky-mid) 40%, var(--ocean) 72%, var(--navy) 90%, var(--black) 100%);
  }

  .brand-name {
    position: absolute;
    top: 82px;
    left: 0;
    width: 100%;
    text-align: center;
    font-family: "Open Sans", sans-serif;
    font-weight: 700;
    font-size: 36px;
    color: var(--brand-ink);
  }

  .product-title {
    position: absolute;
    top: 170px;
    left: 0;
    width: 100%;
    text-align: center;
    font-family: "Russo One", sans-serif;
    font-weight: 400;
    line-height: 1;
  }

  .product-title span {
    display: block;
    transform: scaleX(1.22);
    transform-origin: center;
    -webkit-text-stroke: 3px var(--outline-dark);
    paint-order: stroke fill;
    text-shadow: 2px 2px 0 var(--white), -2px -2px 0 var(--white), 2px -2px 0 var(--white), -2px 2px 0 var(--white);
  }

  .title-line-1 { font-size: 44px; color: var(--heading-orange); letter-spacing: 2px; }
  .title-line-2 { font-size: 37px; color: var(--heading-yellow); letter-spacing: 2px; margin-top: 2px; }
  .title-line-3 { font-size: 31px; color: var(--heading-red); letter-spacing: 2px; margin-top: 12px; }
  .title-line-4 { font-size: 31px; color: var(--heading-red); letter-spacing: 2px; margin-top: 0; }

  .product-photo {
    position: absolute;
    left: 33px;
    top: 339px;
    width: 440px;
    height: 177px;
    border-radius: 40px 60px 30px 30px;
    background:
      linear-gradient(180deg, rgba(0,0,0,0) 0%, rgba(0,0,0,0) 78%, rgba(40,40,40,0.55) 100%),
      radial-gradient(ellipse 30% 30% at 45% 15%, var(--photo-roof), rgba(181,74,74,0) 100%),
      linear-gradient(180deg, var(--photo-top) 0%, var(--photo-mid) 100%);
  }

  .tagline {
    position: absolute;
    top: 534px;
    left: 0;
    width: 100%;
    text-align: center;
    font-family: "Open Sans", sans-serif;
    font-style: italic;
    font-weight: 800;
    font-size: 18px;
    color: var(--tag-yellow);
    -webkit-text-stroke: 0.6px var(--outline-dark);
    text-shadow: 1px 1px 0 var(--outline-dark);
  }

  .yield-badge {
    position: absolute;
    left: 68px;
    top: 569px;
    width: 94px;
    height: 94px;
  }

  .benefit-list {
    position: absolute;
    left: 236px;
    top: 578px;
    width: 208px;
    display: grid;
    grid-template-columns: 1fr 1fr;
    list-style: none;
    border-top: 1.5px solid var(--rule-blue);
  }

  .benefit-list li {
    font-family: "Open Sans", sans-serif;
    font-weight: 700;
    font-size: 18px;
    line-height: 24px;
    color: var(--white);
    border-bottom: 1.5px solid var(--rule-blue);
    padding-left: 4px;
    white-space: nowrap;
  }

  .benefit-list li::before {
    content: "";
    display: inline-block;
    width: 6px;
    height: 6px;
    background: var(--bullet-orange);
    margin-right: 9px;
    vertical-align: middle;
    position: relative;
    top: -2px;
  }
</style>
</head>
<body>
<div class="artboard">
  <p class="spec-note">Label dimensions 75mm x 107mm</p>

  <section class="label">
    <p class="brand-name">Brightwell Care</p>

    <h1 class="product-title">
      <span class="title-line-1">HEAVY DUTY</span>
      <span class="title-line-2">CONVERTIBLE</span>
      <span class="title-line-3">SOFT TOP</span>
      <span class="title-line-4">CLEANER</span>
    </h1>

    <div class="product-photo" role="img" aria-label="Photo of a white convertible sports car with a red soft top, seen from the rear three-quarter view"></div>

    <p class="tagline">Quick and easy to use for professional results</p>

    <svg class="yield-badge" viewBox="0 0 94 94" aria-label="Makes 2 litres">
      <circle cx="49" cy="49" r="44" fill="#1b1b1b"/>
      <circle cx="46" cy="46" r="44" fill="var(--white)"/>
      <circle cx="46" cy="46" r="39" fill="var(--badge-pink)"/>
      <g transform="rotate(-20 46 46)" font-family="Open Sans, sans-serif" font-weight="800" fill="var(--white)" text-anchor="middle">
        <text x="46" y="29" font-size="12">MAKES</text>
        <text x="46" y="60" font-size="32">2</text>
        <text x="46" y="74" font-size="12">LITRES</text>
      </g>
    </svg>

    <ul class="benefit-list">
      <li>CLEAN</li>
      <li>STAINS</li>
      <li>DIRT</li>
      <li>MOULD</li>
      <li>GRIME</li>
      <li>MILDEW</li>
    </ul>
  </section>
</div>
</body>
</html>
```